Graphics for website image slider

We need 4 banners for website:

We provide software development services to very small to large Businesses. The focus of these 4 banners is to portray the four steps approach to our consulting process: Assess, Analyse, Plan and Deploy

Currently we have the following on our website:
http://www.lumertix.com

We are redesigning the website and want to use 4 sliding graphics to portray the same thing, and the new site is being designed here:
http://www.lumertixonline.com/lumertix

You can use stock photos for each banner or your own creativity.

The images should be 1140px wide and about 420px High.

You can use any modern font such as google font. Not just curly fonts!

Reason: Not yet able to select the final design.

I have updated the colors and how they are supposed to flow because I noticed that some designs did not follow that (We are consultants and really want to understand our process in a powerful way):

ASSESS: Orange color (1st or 5th color above)

ANALYSE: Yellow (2nd or 6th color above)

PLAN: Green (3rd or 7th color above)

DEPLOY: Blue (4th or 8th color above)

=================================================

Some designers also made mistakes in typing the text (Please copy and paste from below):

ASSESS

We gather information and data

to identify and delineate

your central and most pressing business and IT issues.

ANALYSE

We show you exactly where you are in terms of IT maturity

using our optimization tools.

We then build an IT roadmap to help you get to the next level.

PLAN:

We identify the IT products and processes necessary to implement the solution.

We then create a detailed plan of action and technical specifications.

DEPLOY

Finally, we utilize industry best practices and repeatable development and

deployment methods to ensure efficiency and high quality results

that satisfy and bring improvement within budget and timeline.

                                   

Target Market(s)

http://www.lumertix.com

Industry/Entity Type

Software

Font styles to use
Sans Serif
Other font styles liked:
• Any other modern font (No curly fonts)

Colors
fee18a
fbf289
cadf82
86cae6
f78f20
ffc214
9aca3c
0692cd

Requirements
Must have
• Graphic should convey the message for each process

```html
<!DOCTYPE html>
<html lang="en">
<head>
<meta charset="utf-8">
<title>Deploy – Slider Banner</title>
<link href="https://fonts.googleapis.com/css2?family=Open+Sans:wght@600;700&display=swap" rel="stylesheet">
<style>
  :root {
    --banner-blue: #0692cd;
    --heading-ink: #2f3133;
    --body-ink: #23282c;
    --button-bg: #ffffff;
    --button-ink: #111111;
    --piece-green: #5aa800;
    --piece-red: #e60a0a;
    --piece-yellow: #f5e40e;
    --piece-blue: #0a3fd0;
  }
  html, body {
    margin: 0;
    padding: 0;
    width: 1200px;
    height: 453px;
    overflow: hidden;
  }
  .slide-banner {
    position: relative;
    width: 1200px;
    height: 453px;
    background: var(--banner-blue);
    font-family: "Open Sans", Arial, sans-serif;
  }
  .slide-copy {
    position: absolute;
    left: 152px;
    top: 112px;
    width: 500px;
  }
  .slide-title {
    margin: 0;
    font-size: 58px;
    font-weight: 700;
    line-height: 1;
    color: var(--heading-ink);
  }
  .slide-text {
    margin: 18px 0 0;
    font-size: 15.5px;
    font-weight: 700;
    line-height: 19px;
    color: var(--body-ink);
  }
  .cta-button {
    display: flex;
    align-items: center;
    justify-content: center;
    margin-top: 18px;
    width: 233px;
    height: 60px;
    background: var(--button-bg);
    color: var(--button-ink);
    font-size: 21px;
    font-weight: 700;
    text-decoration: none;
    border-radius: 2px;
  }
  .process-visual {
    position: absolute;
    left: 740px;
    top: 74px;
    width: 314px;
    height: 315px;
    background: linear-gradient(135deg,
      var(--piece-green) 0%,
      var(--piece-red) 35%,
      var(--piece-yellow) 62%,
      var(--piece-blue) 100%);
  }
</style>
</head>
<body>
  <section class="slide-banner">
    <div class="slide-copy">
      <h1 class="slide-title">DEPLOY</h1>
      <p class="slide-text">Finally, we utilize industry best practices and repeatable development and deployment methods to ensure efficiency and high quality results that satisfy and bring improvement within budget and timeline.</p>
      <a class="cta-button" href="#">GET STARTED</a>
    </div>
    <div class="process-visual" role="img" aria-label="Four puzzle pieces in green, red, yellow and blue joined into a square frame"></div>
  </section>
</body>
</html>
```